Lanternfield Billboard - Financial Services Company (Investments, Tax Planning and Insurance)

Our new office has a billboard directly above the office building. We'd like something eye-catching with a strong Call to Action, with the main part of the billboard being under 7 words if possible. We'd like you to include a way to get ahold of us (either our website lanternfieldllc.example or our phone number 302-418-2967. You may also include in small font something to indicate that we've been serving the area since 1980 (the DE area, the tri-state area, the Copperleaf Basin, etc.)

We offer financial planning, tax planning, and insurance, and we help our clients to focus on their goals and happiness by providing everything they need for lifelong wealth under one roof.

Our logos are attached, we use a triangle logo with green and gray. We use the tagline "experience lifelong wealth" but this does not need to be included.

Potential ideas we have seen from other financial companies-
- the concept that the driver spends more time looking at billboards than planning for their retirement
-something along the lines of "everything you need for your finances is in this building right here" planning, investments, taxes, insurance"
-don't spend your time worrying about retirement, let us help you plan for it
-are you working for your money, or is it working for you?
- retirement takes planning, we're here to help
- ready to retire? talk to us
- need investment advice?
- need help investing?
- crossing your fingers isn't a retirement plan. we can help.
- retiring soon? you need help.

Those are just general ideas, please feel free to be creative.

brand colors:
#00b585
#00b185
#000000
#ffffff
#6d6f75
#6d6f75
#6f7074
#021712
#052e24

```html
<!DOCTYPE html>
<html lang="en">
<head>
<meta charset="utf-8">
<title>Lanternfield Billboard</title>
<link href="https://fonts.googleapis.com/css2?family=Montserrat:wght@500;600;700;800&family=Dosis:wght@500;700&display=swap" rel="stylesheet">
<style>
  :root {
    --green: #00b585;
    --green-soft: #1bc090;
    --green-deep: #052e24;
    --ink: #021712;
    --black: #000000;
    --white: #ffffff;
    --gray: #6d6f75;
    --page: #e6e9e8;
  }
  * { margin: 0; padding: 0; box-sizing: border-box; }
  html, body { width: 1040px; height: 1200px; overflow: hidden; background: var(--page); }
  .billboard {
    position: absolute; left: 0; top: 340px;
    width: 1040px; height: 520px; overflow: hidden;
    font-family: "Montserrat", sans-serif;
  }
  .photo {
    position: absolute; inset: 0;
    background:
      radial-gradient(ellipse 220px 180px at 700px 340px, rgba(196,140,110,.55), transparent 70%),
      linear-gradient(100deg, #2e3133 0%, #4a4e51 30%, #9aa2a6 55%, #dfe5e8 75%, #f3f5f6 100%);
  }
  .shapes { position: absolute; inset: 0; }
  .headline {
    position: absolute; left: 46px; top: 38px;
    font-weight: 800; font-size: 52px; line-height: 57px;
    letter-spacing: 1px; color: var(--white);
  }
  .headline .accent { color: var(--green); }
  .since {
    position: absolute; left: 110px; top: 252px;
    font-family: "Dosis", sans-serif; font-weight: 500;
    font-size: 28px; color: var(--white); letter-spacing: .5px;
  }
  .since b { font-weight: 700; }
  .brand {
    position: absolute; right: 35px; top: 36px;
    display: flex; align-items: center; gap: 10px;
    font-weight: 700; font-size: 44px; line-height: 1; color: var(--green);
  }
  .brand-mark { width: 30px; height: 30px; background: var(--gray); }
  .contact {
    position: absolute; top: 472px;
    display: flex; align-items: center; gap: 12px;
    font-weight: 700; color: var(--white);
  }
  .contact svg { width: 26px; height: 26px; flex: none; }
  .contact-phone { left: 62px; font-size: 20px; letter-spacing: 4px; }
  .contact-web { left: 392px; font-size: 18px; letter-spacing: 2px; }
</style>
</head>
<body>
  <div class="billboard">
    <div class="photo" role="img" aria-label="Photo of two businesspeople shaking hands in a bright office"></div>

    <svg class="shapes" viewBox="0 0 1040 520" width="1040" height="520">
      <path d="M0 210 L60 210 Q80 210 70 230 L30 290 L0 330 Z" fill="#ffffff" opacity=".28"/>
      <path d="M0 0 H556 L290 268 Q258 300 218 316 Q205 322 192 318 L0 245 Z" fill="var(--ink)" opacity=".93"/>
      <path d="M75 242 H273 L273 291 H120 Z" fill="var(--green-deep)"/>
      <path d="M446 236 L424 259 L446 282" fill="none" stroke="var(--green)" stroke-width="14" stroke-linecap="round" stroke-linejoin="round"/>
      <path d="M0 457 H789 L735 520 H0 Z" fill="var(--green-deep)" opacity=".95"/>
      <path d="M729 520 L985 305 Q1020 280 1040 300 V520 Z" fill="var(--green-soft)"/>
      <path d="M820 520 L1040 360 V520 Z" fill="var(--green)" opacity=".7"/>
    </svg>

    <h1 class="headline">NEED<br><span class="accent">INVESTMENT</span><br>ADVICE</h1>
    <p class="since">SINCE <b>1980</b></p>

    <div class="brand"><span class="brand-mark"></span>Lanternfield</div>

    <div class="contact contact-phone">
      <svg viewBox="0 0 26 26"><circle cx="13" cy="13" r="11.5" fill="none" stroke="#fff" stroke-width="2"/><path d="M9 7.5 L11 7 L12.3 10 L11 11.2 Q12.3 14 14.8 15.2 L16 13.9 L19 15.2 L18.5 17.2 Q17.5 18.5 15.5 18 Q10.5 16 8.2 11 Q7.6 8.8 9 7.5 Z" fill="#fff"/></svg>
      <span>302-418-2967</span>
    </div>
    <div class="contact contact-web">
      <svg viewBox="0 0 26 26"><circle cx="13" cy="13" r="11.5" fill="none" stroke="#fff" stroke-width="2"/><circle cx="13" cy="13" r="7" fill="none" stroke="#fff" stroke-width="1.5"/><ellipse cx="13" cy="13" rx="3" ry="7" fill="none" stroke="#fff" stroke-width="1.5"/><path d="M6 13 H20 M7.5 9.5 H18.5 M7.5 16.5 H18.5" stroke="#fff" stroke-width="1.3"/></svg>
      <span>lanternfieldllc.example</span>
    </div>
  </div>
</body>
</html>
```